Pine Hill Drafting - Flyer Design

I'm looking for good designs of the 2 sided flyer size DL (210 x 95 mm)
Please make sure the design is in the same colours as my business card. Image attached.
Include Architectural plan at the background.
Please note that some words are in capital letters...
FRONT PAGE including :
Are you planning to RENOVATE, EXTEND the house, build new GRANNY FLAT?
Do you need assistance with DA , COMPLYING DEVELOPMENT?
Is your building budget tight and you DON'T WANT to spend it on the ARCHITECTURAL FEES?
For free obligation quote contact:
PINE HILL DRAFTING
pinehilldrafting@mailnest.net.au
Dorte - 0482 657 930
For more details check: www.pinehilldrafting.net.au
Follow us on chatterly: www.chatterly.net/pinehilldrafting
BACK PAGE including:
Services
- Building Design
- Architectural Drafting
- 3D Modelling
- Norvo Assessment
- Building Specifications
- Council Submission Services
- Coordination with Building Professionals
Contact Dorte on 0482 657 930 or pinehilldrafting@mailnest.net.au for obligation free quote

```html
<!DOCTYPE html>
<html lang="en">
<head>
<meta charset="utf-8">
<title>Pine Hill Drafting – DL Flyer</title>
<link rel="stylesheet" href="https://fonts.googleapis.com/css2?family=Source+Sans+3:wght@400;600;700&display=swap">
<style>
  :root {
    --brand-blue: #1ba6dc;
    --ink: #2b2b2b;
    --paper: #ffffff;
    --mist-top: #ffffff;
    --mist-bottom: #ebebec;
    --canvas: #f2f2f2;
  }
  * { box-sizing: border-box; margin: 0; padding: 0; }
  html, body {
    width: 1118px; height: 1200px; overflow: hidden;
    background: var(--canvas);
    font-family: "Source Sans 3", "Myriad Pro", Arial, sans-serif;
    color: var(--ink);
  }
  .spread {
    position: absolute; top: 138px; left: 109px;
    display: flex; gap: 60px;
  }
  .flyer {
    width: 420px; height: 924px;
    background: var(--paper);
    display: flex; flex-direction: column;
    box-shadow: 0 2px 10px rgba(0,0,0,0.12);
  }
  .flyer__title {
    font-weight: 700; font-size: 31px; letter-spacing: 0.2px;
    text-align: center;
  }
  /* Front */
  .front .flyer__title {
    height: 96px; line-height: 96px; color: var(--brand-blue);
  }
  .front .plan-art {
    height: 397px;
    background: linear-gradient(160deg, #fdfdfd 0%, #eceef0 45%, #d9dcdf 100%);
  }
  .front .questions {
    flex: 1;
    background: linear-gradient(var(--mist-top), var(--mist-bottom));
    padding: 26px 26px 0 24px;
  }
  .question {
    display: flex; gap: 12px; font-size: 19px; line-height: 1.22;
    margin-bottom: 22px;
  }
  .question::before {
    content: ""; flex: 0 0 17px; height: 17px; margin-top: 3px;
    background: var(--brand-blue);
  }
  .contact {
    text-align: center; font-size: 15.5px; line-height: 1.3;
  }
  .contact__name { color: var(--brand-blue); }
  .contact__person { font-weight: 700; }
  .front .contact { margin-top: 14px; }
  .flyer__footer {
    height: 62px; background: var(--brand-blue); color: #fff;
    font-weight: 600; font-size: 12.5px; line-height: 1.3;
    display: flex; flex-direction: column; justify-content: center; align-items: center;
  }
  /* Back */
  .back .flyer__title {
    height: 99px; line-height: 99px; background: var(--brand-blue); color: #fff;
    font-size: 32px;
  }
  .back .house-art {
    height: 319px;
    background: linear-gradient(180deg, #ffffff 0%, #f1f2f3 60%, #e4e6e8 100%);
  }
  .services {
    height: 322px; background: var(--brand-blue); color: #fff;
    padding: 26px 20px 0 22px;
  }
  .services__heading { font-size: 19px; margin-bottom: 26px; }
  .services__list { list-style: none; padding-left: 18px; }
  .services__item {
    display: flex; align-items: center; gap: 7px;
    font-size: 18.5px; line-height: 29.5px;
  }
  .services__tick { width: 15px; height: 15px; flex: 0 0 15px; }
  .back .contact-panel {
    flex: 1;
    background: linear-gradient(var(--mist-bottom), var(--mist-top));
    padding-top: 28px;
  }
</style>
</head>
<body>
<main class="spread">
  <section class="flyer front">
    <h1 class="flyer__title">PINE HILL DRAFTING</h1>
    <div class="plan-art" role="img" aria-label="Rolled architectural floor plan sheets"></div>
    <div class="questions">
      <p class="question"><span>Are you planning to RENOVATE, EXTEND the house, build new GRANNY FLAT?</span></p>
      <p class="question"><span>Do you need assistance with DA , COMPLYING DEVELOPMENT?</span></p>
      <p class="question"><span>Is your building budget tight and you DON'T WANT to spend it on the ARCHITECTURAL FEES?</span></p>
      <div class="contact">
        <p>For free obligation quote contact:</p>
        <p class="contact__name">PINE HILL DRAFTING</p>
        <p>pinehilldrafting@mailnest.net.au</p>
        <p class="contact__person">Dorte - 0482 657 930</p>
      </div>
    </div>
    <footer class="flyer__footer">
      <p>For more details check: www.pinehilldrafting.net.au</p>
      <p>Follow us on chatterly: www.chatterly.net/pinehilldrafting</p>
    </footer>
  </section>

  <section class="flyer back">
    <h2 class="flyer__title">PINE HILL DRAFTING</h2>
    <div class="house-art" role="img" aria-label="Line drawing of a modern single-storey house with flat roof and front steps"></div>
    <div class="services">
      <p class="services__heading">SERVICES:</p>
      <ul class="services__list">
        <li class="services__item"><svg class="services__tick" viewBox="0 0 16 16"><path d="M2 8.5l4 4 8-9" fill="none" stroke="#fff" stroke-width="2.4"/></svg>Building Design</li>
        <li class="services__item"><svg class="services__tick" viewBox="0 0 16 16"><path d="M2 8.5l4 4 8-9" fill="none" stroke="#fff" stroke-width="2.4"/></svg>Architectural Drafting</li>
        <li class="services__item"><svg class="services__tick" viewBox="0 0 16 16"><path d="M2 8.5l4 4 8-9" fill="none" stroke="#fff" stroke-width="2.4"/></svg>3D Modelling</li>
        <li class="services__item"><svg class="services__tick" viewBox="0 0 16 16"><path d="M2 8.5l4 4 8-9" fill="none" stroke="#fff" stroke-width="2.4"/></svg>Norvo Assessment</li>
        <li class="services__item"><svg class="services__tick" viewBox="0 0 16 16"><path d="M2 8.5l4 4 8-9" fill="none" stroke="#fff" stroke-width="2.4"/></svg>Building Specifications</li>
        <li class="services__item"><svg class="services__tick" viewBox="0 0 16 16"><path d="M2 8.5l4 4 8-9" fill="none" stroke="#fff" stroke-width="2.4"/></svg>Council Submission Services</li>
        <li class="services__item"><svg class="services__tick" viewBox="0 0 16 16"><path d="M2 8.5l4 4 8-9" fill="none" stroke="#fff" stroke-width="2.4"/></svg>Coordination with Building Professionals</li>
      </ul>
    </div>
    <div class="contact-panel">
      <div class="contact">
        <p>For free obligation quote contact:</p>
        <p class="contact__name">PINE HILL DRAFTING</p>
        <p>pinehilldrafting@mailnest.net.au</p>
        <p class="contact__person">Dorte - 0482 657 930</p>
      </div>
    </div>
    <footer class="flyer__footer">
      <p>For more details check: www.pinehilldrafting.net.au</p>
      <p>Follow us on chatterly: www.chatterly.net/pinehilldrafting</p>
    </footer>
  </section>
</main>
</body>
</html>
```